Need to drive pregnant women to my 3d4d ultrasound studio where i provide 4d ultrasound with hyperalistic imaging and gender reveals

Industry/Entity Type

Healthcare

Font styles to use
Decorative
Script

Requirements
Must have
• My Company name Latido de Luna 4D. EVERYTHING HAS TO BE IN SPANISH
Nice to have
• SIMPLE AND NOT TOO BUSY
Should not have
• website

```html
<!DOCTYPE html>
<html lang="es">
<head>
<meta charset="utf-8">
<title>Latido de Luna 4D – Banner</title>
<link rel="stylesheet" href="https://fonts.googleapis.com/css2?family=Great+Vibes&family=Lobster&display=swap">
<style>
  :root {
    --page-bg: #d4d4d4;
    --banner-white: #ffffff;
    --banner-sky: #a9d6ef;
    --title-magenta: #c4175f;
    --tagline-navy: #10125e;
    --art-rose: #e2456f;
    --art-pink: #f29bb0;
    --art-blush: #fbe3ea;
    --scan-dark: #0b0d12;
    --scan-amber: #b8702e;
    --scan-deep: #5a2e10;
    --baby-skin: #e9b9a2;
    --baby-shade: #c98e78;
  }
  * { margin: 0; padding: 0; box-sizing: border-box; }
  html, body {
    width: 1200px;
    height: 1165px;
    overflow: hidden;
    background: var(--page-bg);
  }
  .canvas {
    position: relative;
    width: 1200px;
    height: 1165px;
  }
  .banner {
    position: absolute;
    left: 20px;
    top: 413px;
    width: 1160px;
    height: 338px;
    overflow: hidden;
    background: linear-gradient(90deg, var(--banner-white) 0%, #eef7fc 45%, var(--banner-sky) 100%);
  }
  .bouquet-art {
    position: absolute;
    left: 0;
    top: 0;
    width: 172px;
    height: 338px;
    background: linear-gradient(180deg, var(--art-rose) 0%, var(--art-pink) 55%, var(--art-blush) 100%);
  }
  .brand-name {
    position: absolute;
    left: 497px;
    top: 96px;
    transform: translateX(-50%);
    white-space: nowrap;
    font-family: "Great Vibes", cursive;
    font-weight: 400;
    font-size: 90px;
    line-height: 1;
    color: var(--title-magenta);
  }
  .tagline {
    position: absolute;
    left: 497px;
    top: 206px;
    transform: translateX(-50%);
    white-space: nowrap;
    text-align: center;
    font-family: "Lobster", cursive;
    font-size: 27px;
    line-height: 37px;
    color: var(--tagline-navy);
  }
  .scan-screen {
    position: absolute;
    left: 888px;
    top: 11px;
    width: 192px;
    height: 150px;
    transform: rotate(2deg);
    background:
      radial-gradient(ellipse at 45% 50%, var(--scan-amber) 0 40%, var(--scan-deep) 70%, transparent 72%),
      var(--scan-dark);
  }
  .photo {
    position: absolute;
    width: 118px;
    height: 142px;
  }
  .photo--scan {
    left: 862px;
    top: 186px;
    transform: rotate(-15deg);
    background: radial-gradient(ellipse at 50% 45%, var(--scan-amber), var(--scan-deep) 85%);
  }
  .photo--newborn {
    left: 987px;
    top: 174px;
    transform: rotate(14deg);
    background: radial-gradient(ellipse at 45% 50%, var(--baby-skin), var(--baby-shade) 90%);
  }
</style>
</head>
<body>
  <main class="canvas">
    <section class="banner">
      <div class="bouquet-art" role="img" aria-label="Ilustración de globos de fiesta con un ramo de peonías rosas"></div>
      <h1 class="brand-name">Latido de Luna 4D</h1>
      <p class="tagline">Ecografías 4D Con Imágenes Hiperrealistas<br>Y Revelación De Género</p>
      <div class="scan-screen" role="img" aria-label="Pantalla de ecógrafo mostrando una ecografía 4D de un bebé"></div>
      <div class="photo photo--scan" role="img" aria-label="Fotografía de ecografía 4D en tonos ámbar"></div>
      <div class="photo photo--newborn" role="img" aria-label="Fotografía de un recién nacido dormido"></div>
    </section>
  </main>
</body>
</html>
```